THE SALT ORCHARD - "Trade" size book cover design for a novel

THE SALT ORCHARD is a thriller that explores what happens at THE SALT ORCHARD life and death. I'd like to see a cover that reflects the near death experience scenes, but I am open to any creative cover that reflects the theme of the book and the sample scenes that I have attached. Please read the scenes.
Space should be left on the cover for the typical promotional text, etc.

NOVEL SUMMARY - Dr. Dorian Fellwick is skeptical of the afterlife. He doesn't believe he will be reunited with his wife, or joined with God in heaven. What he knows, or thinks he knows, is that he should have seen the warning signs of his wife's heart attack, should have saved her. After four years of mourning, Dorian is finally moving on, succumbing to lust and longing, instead of sorrow. Still he fears the little mistakes that can kill, like a missed diagnosis, or the slip of a scalpel -- the kind of mistakes that depression feeds. When he dates the mother of an epileptic patient, he begins to believe that death will finally stop controlling his life. He has no idea, that the woman of his desires has killed her first husband, and will soon kill her son. As Dorian falls in love and marries, he also becomes involved in a clinical study of near death experiences. Life and research are about to collide.
Updates

The designs I have seen so far are quite dark and seem like they would better fit a horror novel. I am looking for something that is more beautiful. The near death experience scenes in the book are hopeful and wonderous. I also would prefer not to have a dark tunnel representing near death. Moths can also be beautiful creatures. I attached scenes from the book in the original post that might be helpful.

You don't have to use the moth as the focal point, or you might want to use moths as they appear in the main near death scene. I am not wedded to that idea.

Here are some additional ideas for designs: 1. At the climax of the book, there is a scene (see attachment) where there is a fight, and the main character's wife tries to kill him. In that scene, the main character breaks a picture frame with a Hercules Moth specimen over his wife's head. Perhaps a design could incorporate broken glass on the floor with the moth, in whole or part. It could even have a woman's foot wearing and athletic or bicycle shoe stepping on the glass. 2. In the scene where the main character has a near death experience (see attachment), there are vivid surreal descriptions of what he sees, including fluttering moths, numbers and colors. There are also visions of other souls represented as points of light. If this can be represented kind of like a representation of curvatures in space time, all the better. 3. When the main character is a boy, he is slightly autistic and is mesmerized by counting the leaves within a forest tall trees. That could be one possibility for a background. 4. When the main character and wife or on a bicycle vacation in Tuscany, they come across a vineyard after it rains. At the end of one of the vineyard rows, there is a beautiful multicolor rose bush. With droplets of water clinging to the petals. Perhaps there can be reflections in the water drops of moths, or something else (even if it is just light.)

Target Market(s)

Book Readers - Thrillers, suspense, near death experiences, medical(neurology).

Colors

Designer to choose colors to be used in the design.

Requirements
Must have
• Creative design that fits the theme of book. It should not be too dark and brooding (it is not a horror story.) It also should not look like a romance cover.
Nice to have
• One or more of the following as reflected in the attached scenes - Moths, (including Hercules moth); a silhouette of a middle aged bald man perhaps floating in the clouds, shards of broken glass from the picture frame in the climatic scene (not tempered glass from a windshield), near death graphics (not a dark tunnel), time/space or theoretical inspired graphic , the feeling of being caught between two worlds, tree canopy with lots of leaves; enlarged crystaline snow flakes each incorporating a symbol (such a pi, a circle with concentric octagons --ancient method of calculating area of circle, representations or pictures of moths, the symbol for infinity, shards of broken glass, prime numbers, bubbles of color. I am also not opposed to other abstract ideas.
Should not have
• Dark tunnels to represent near death.
• Romance novel cover or overly romantic.
• Horror type novel.

```html
<!DOCTYPE html>
<html lang="en">
<head>
<meta charset="utf-8">
<title>The Salt Orchard — Book Cover</title>
<link rel="stylesheet" href="https://fonts.googleapis.com/css2?family=Cinzel:wght@400;500&family=Cormorant+Garamond:ital,wght@1,500;1,600&display=swap">
<style>
  :root {
    --sky-top: #4f6079;
    --sky-mid: #a9a39a;
    --sky-warm: #dccbaf;
    --floor: #ebe3d6;
    --title-white: #f7f4ef;
    --title-accent: #7a5148;
    --author: #6f5662;
    --frame-light: #c9c9cc;
    --frame-dark: #4f525b;
    --glass-warm: #d2b68c;
    --moth-tone: #a27e6c;
    --glow: rgba(255, 252, 240, 0.9);
  }
  html, body {
    margin: 0;
    padding: 0;
    width: 795px;
    height: 1200px;
    overflow: hidden;
    background: #ffffff;
  }
  .cover {
    position: relative;
    width: 795px;
    height: 1200px;
    overflow: hidden;
  }
  .cover-sky {
    position: absolute;
    inset: 0;
    background:
      radial-gradient(ellipse 330px 230px at 300px 660px, rgba(255,252,240,0.85), rgba(255,252,240,0) 70%),
      radial-gradient(ellipse 500px 140px at 100px 250px, rgba(60,76,98,0.45), rgba(60,76,98,0) 70%),
      radial-gradient(ellipse 420px 160px at 720px 200px, rgba(60,76,98,0.5), rgba(60,76,98,0) 70%),
      radial-gradient(ellipse 420px 120px at 400px 560px, rgba(190,170,140,0.35), rgba(190,170,140,0) 70%),
      linear-gradient(180deg, var(--sky-top) 0%, #7b8592 13%, var(--sky-mid) 27%, var(--sky-warm) 45%, #e4d7c2 66%, var(--floor) 100%);
  }
  .cover-rays {
    position: absolute;
    left: 190px;
    top: 0;
    width: 380px;
    height: 560px;
    background:
      linear-gradient(100deg, rgba(255,255,255,0) 30%, rgba(255,255,255,0.28) 38%, rgba(255,255,255,0) 44%, rgba(255,255,255,0.22) 52%, rgba(255,255,255,0) 58%, rgba(255,255,255,0.18) 66%, rgba(255,255,255,0) 74%);
    -webkit-mask-image: linear-gradient(180deg, #000 20%, transparent 100%);
    mask-image: linear-gradient(180deg, #000 20%, transparent 100%);
  }
  .cover-particles {
    position: absolute;
    inset: 0;
    background:
      radial-gradient(circle 5px at 118px 945px, rgba(255,255,255,0.9), transparent),
      radial-gradient(circle 4px at 40px 725px, rgba(255,255,255,0.85), transparent),
      radial-gradient(circle 3px at 690px 740px, rgba(255,255,255,0.85), transparent),
      radial-gradient(circle 4px at 660px 690px, rgba(255,255,255,0.8), transparent),
      radial-gradient(circle 3px at 760px 620px, rgba(255,255,255,0.8), transparent),
      radial-gradient(circle 3px at 200px 880px, rgba(255,255,255,0.8), transparent),
      radial-gradient(circle 3px at 300px 860px, rgba(255,255,255,0.8), transparent),
      radial-gradient(circle 2px at 620px 790px, rgba(255,255,255,0.8), transparent),
      radial-gradient(circle 3px at 560px 880px, rgba(255,255,255,0.8), transparent),
      radial-gradient(circle 2px at 90px 800px, rgba(255,255,255,0.8), transparent),
      radial-gradient(circle 3px at 730px 540px, rgba(255,255,255,0.7), transparent),
      radial-gradient(circle 2px at 160px 600px, rgba(255,255,255,0.7), transparent);
  }
  .cover-glass-floor {
    position: absolute;
    left: 0;
    top: 960px;
    width: 795px;
    height: 140px;
    background: radial-gradient(ellipse 360px 70px at 370px 70px, rgba(255,255,255,0.55), rgba(255,255,255,0) 75%);
  }
  .frame-art {
    position: absolute;
    left: 0;
    top: 0;
    width: 795px;
    height: 1200px;
  }
  .title {
    position: absolute;
    left: 0;
    right: 0;
    top: 36px;
    margin: 0;
    text-align: center;
    font-weight: 400;
  }
  .title-article {
    display: block;
    font-family: 'Cormorant Garamond', serif;
    font-style: italic;
    font-weight: 600;
    font-size: 64px;
    line-height: 72px;
    letter-spacing: 4px;
    color: var(--title-accent);
  }
  .title-line {
    display: block;
    font-family: 'Cinzel', serif;
    font-weight: 400;
    font-size: 112px;
    line-height: 124px;
    letter-spacing: 10px;
    color: var(--title-white);
    text-shadow: 0 1px 6px rgba(80,80,90,0.25);
  }
  .review {
    position: absolute;
    top: 436px;
    width: 204px;
    text-align: center;
    color: var(--title-white);
  }
  .review-left { left: 38px; }
  .review-right { left: 540px; }
  .review-stars {
    display: block;
    font-size: 31px;
    letter-spacing: 5px;
    line-height: 34px;
  }
  .review-source {
    display: block;
    margin-top: 6px;
    font-family: 'Cormorant Garamond', serif;
    font-style: italic;
    font-weight: 500;
    font-size: 21px;
    line-height: 23px;
    letter-spacing: 2px;
    text-transform: uppercase;
  }
  .author {
    position: absolute;
    left: 0;
    right: 0;
    bottom: 4px;
    margin: 0;
    text-align: center;
    font-family: 'Cinzel', serif;
    font-weight: 400;
    font-size: 82px;
    line-height: 86px;
    letter-spacing: 6px;
    color: var(--author);
  }
</style>
</head>
<body>
  <main class="cover">
    <div class="cover-sky" role="img" aria-label="Clouded sky opening onto a pale, glowing horizon"></div>
    <div class="cover-rays" role="img" aria-label="Soft beams of light falling from the clouds"></div>
    <div class="cover-glass-floor" role="img" aria-label="Shards of broken glass scattered on the floor"></div>
    <div class="cover-particles" role="img" aria-label="Floating specks of light"></div>

    <svg class="frame-art" viewBox="0 0 795 1200" role="img" aria-label="Tilted ornate picture frame standing on one corner, holding a moth specimen behind cracked glass">
      <defs>
        <linearGradient id="frameEdge" x1="0" y1="0" x2="1" y2="1">
          <stop offset="0" stop-color="var(--frame-light)" stop-opacity="0.35"/>
          <stop offset="0.5" stop-color="#8d8f96"/>
          <stop offset="1" stop-color="var(--frame-dark)"/>
        </linearGradient>
        <linearGradient id="glassFill" x1="0" y1="0" x2="1" y2="1">
          <stop offset="0" stop-color="#f6efe0" stop-opacity="0.6"/>
          <stop offset="0.5" stop-color="var(--glass-warm)"/>
          <stop offset="1" stop-color="#b59468"/>
        </linearGradient>
        <radialGradient id="mothTone" cx="0.5" cy="0.5" r="0.5">
          <stop offset="0" stop-color="var(--moth-tone)" stop-opacity="0.75"/>
          <stop offset="1" stop-color="var(--moth-tone)" stop-opacity="0"/>
        </radialGradient>
        <radialGradient id="frameGlow" cx="0.5" cy="0.5" r="0.5">
          <stop offset="0" stop-color="var(--glow)"/>
          <stop offset="1" stop-color="rgba(255,252,240,0)"/>
        </radialGradient>
      </defs>
      <polygon points="365,399 610,832 365,1077 224,684" fill="url(#frameEdge)"/>
      <polygon points="365,430 586,831 369,1049 249,688" fill="#9fa1a7" opacity="0.6"/>
      <polygon points="366,446 572,831 370,1034 262,690" fill="url(#glassFill)"/>
      <ellipse cx="385" cy="770" rx="95" ry="125" fill="url(#mothTone)"/>
      <ellipse cx="300" cy="640" rx="120" ry="110" fill="url(#frameGlow)"/>
      <ellipse cx="365" cy="1080" rx="70" ry="6" fill="#3c3c44" opacity="0.35"/>
    </svg>

    <h1 class="title">
      <span class="title-article">The</span>
      <span class="title-line">SALT</span>
      <span class="title-line">ORCHARD</span>
    </h1>

    <div class="review review-left">
      <span class="review-stars">★★★★★</span>
      <span class="review-source">Harbor<br>Ledger</span>
    </div>
    <div class="review review-right">
      <span class="review-stars">★★★★★</span>
      <span class="review-source">The<br>Meridian</span>
    </div>

    <p class="author">AUTHOR NAME</p>
  </main>
</body>
</html>
```